I need a direct mail postcard made up for my marketing campaign

I am starting a marketing campaign and need a design for a post card. I own an iron door company and need to have before and after images on the post card to showcase what our work looks like. I have provided pictures to use below.

The design needs to be two sided. The logo should be on the front.

The tag line for this campaign is: Design the smile your home deserves.

Words to also use: Distinctive style, Work of Art, One-of-a-Kind, Elegant, Modern, Innovative, Unique

My information for the card
Name: Dean Harlowe
Phone number: (555)-318-2764
Email: Dean@wroughtgatestudio.example

The US postal system is very picky as to what can be sent in the mail. The only requirement they have is for the address. There needs to be a 2inch (50.8mm) by 4inch (101.6mm) blank space on the bottom right hand corner on the back of the card.

Target Market(s)

Home owners

Industry/Entity Type

Home Improvement

Font styles to use
Serif
Decorative

Colors
0555a3
ffffff
ec1f27

Requirements
Must have
• My logo, My contact information, before and after pictures
• Provided 3D images
Nice to have
• Words that describe iron doors
• A contrast between contemporary and ornate doors.

```html
<!DOCTYPE html>
<html lang="en">
<head>
<meta charset="utf-8">
<title>Wrought Gate Studio – Direct Mail Postcard</title>
<link href="https://fonts.googleapis.com/css2?family=Orbitron:wght@700&family=Lato:wght@400;700&display=swap" rel="stylesheet">
<style>
  :root {
    --brand-blue: #0555a3;
    --deep-blue: #04478c;
    --white: #ffffff;
    --ink-grey: #555a60;
    --rule-grey: #c9ccd0;
    --stage: #d9d9d9;
    --paper: #f6f6f6;
    --stamp: #dcdcdc;
    --wood: #4e2610;
    --wood-light: #6e3a1a;
    --glass: #f4f4f4;
  }
  * { box-sizing: border-box; margin: 0; padding: 0; }
  html, body { width: 1200px; height: 1200px; overflow: hidden; }
  body { background: var(--stage); font-family: "Lato", Arial, sans-serif; position: relative; }

  .postcard {
    position: absolute; left: 212px; width: 776px; height: 501px;
    background: linear-gradient(180deg, var(--white) 0%, var(--paper) 55%, var(--white) 100%);
    box-shadow: 3px 4px 6px rgba(0,0,0,.25);
    overflow: hidden;
  }
  .postcard--front { top: 70px; }
  .postcard--back { top: 622px; }
  .postcard > * { position: absolute; }
  .wave { left: 0; top: 0; width: 776px; height: 501px; }

  /* Front */
  .headline {
    left: 29px; top: 23px; font-family: "Orbitron", sans-serif; font-weight: 700;
    font-size: 39.5px; color: var(--brand-blue); letter-spacing: 0.4px; white-space: nowrap; line-height: 1.1;
  }
  .rule { left: 29px; width: 379px; height: 2px; background: var(--brand-blue); }
  .rule--top { top: 78px; }
  .rule--bottom { top: 122px; }
  .subhead {
    left: 29px; top: 84px; font-family: "Orbitron", sans-serif; font-weight: 700;
    font-size: 26.5px; color: var(--ink-grey); white-space: nowrap; line-height: 1.2;
  }
  .feature-row { left: 29px; list-style: none; display: flex; white-space: nowrap; }
  .feature-row--1 { top: 134px; }
  .feature-row--2 { top: 162px; }
  .feature-row li { font-size: 13.5px; color: var(--ink-grey); margin-right: 9px; line-height: 18px; }
  .feature-row li::before { content: "\25C6"; color: var(--brand-blue); font-size: 7px; margin-right: 5px; vertical-align: 2px; }

  .brand-panel {
    left: 589px; top: 0; width: 142px; height: 134px; background: var(--white);
    display: flex; flex-direction: column; align-items: center; justify-content: center; gap: 6px;
  }
  .brand-name {
    font-family: "Lato", sans-serif; font-weight: 700; color: var(--brand-blue);
    text-align: center; text-transform: uppercase; line-height: 1.15;
  }
  .brand-panel .brand-mark { width: 14px; height: 14px; border-radius: 50%; background: var(--brand-blue); }
  .brand-panel .brand-name { font-size: 15px; letter-spacing: 1px; }

  .portrait {
    left: 36px; top: 216px; width: 160px; height: 160px; border-radius: 50%;
    border: 4px solid var(--brand-blue);
    background: radial-gradient(circle at 50% 38%, #d8dce1 0%, #9aa2ab 50%, #26304a 100%);
  }
  .contact { color: var(--white); }
  .contact-name { left: 53px; top: 391px; font-weight: 700; font-size: 19px; }
  .contact-line { left: 53px; font-size: 13.5px; display: flex; align-items: center; gap: 12px; }
  .contact-line svg { width: 11px; height: 11px; fill: var(--white); }
  .contact-line--phone { top: 423px; }
  .contact-line--email { top: 448px; gap: 10px; }

  .door {
    border: 7px solid var(--wood);
    background: linear-gradient(90deg, var(--glass) 0%, #e7e4e1 30%, var(--wood-light) 47%, var(--wood) 50%, var(--wood-light) 53%, #e7e4e1 70%, var(--glass) 100%);
    box-shadow: 0 14px 16px -10px rgba(0,0,0,.35);
  }
  .door--ornate { left: 306px; top: 210px; width: 185px; height: 249px; }
  .door--modern {
    left: 514px; top: 147px; width: 189px; height: 309px;
    background: linear-gradient(90deg, var(--glass) 0%, var(--glass) 22%, var(--wood) 26%, var(--wood-light) 50%, var(--wood) 74%, var(--glass) 78%, var(--glass) 100%);
  }
  .door-floor {
    left: 300px; top: 459px; width: 410px; height: 42px;
    background: linear-gradient(180deg, rgba(255,255,255,.18) 0%, rgba(255,255,255,0) 100%);
  }

  /* Back */
  .gallery-photo { border-right: 4px solid var(--brand-blue); border-bottom: 4px solid var(--brand-blue); }
  .photo-before-1 { left: 16px; top: 15px; width: 130px; height: 213px;
    background: linear-gradient(180deg, #2d1f12 0%, #5a3e1c 22%, #d9c48e 33%, #ece8df 36%, #f6f4ef 100%); }
  .photo-after-1 { left: 162px; top: 14px; width: 132px; height: 216px;
    background: radial-gradient(ellipse at 50% 0%, #d8c9aa 0%, #d8c9aa 18%, #3f3b57 30%, #2c2a3d 70%, #23212f 100%); }
  .photo-before-2 { left: 16px; top: 258px; width: 130px; height: 213px;
    background: linear-gradient(90deg, #4d1c0e 0%, #8b3c20 25%, #5a2414 50%, #8b3c20 75%, #4d1c0e 100%); }
  .photo-after-2 { left: 162px; top: 256px; width: 132px; height: 216px;
    background: linear-gradient(90deg, #1c1b19 0%, #7a5e20 25%, #2a2620 50%, #7a5e20 75%, #1c1b19 100%); }
  .photo-label { font-weight: 700; font-size: 13.5px; color: var(--ink-grey); width: 130px; text-align: center; }
  .label-before-1 { left: 16px; top: 234px; }
  .label-after-1 { left: 164px; top: 234px; }
  .label-before-2 { left: 16px; top: 477px; }
  .label-after-2 { left: 164px; top: 477px; }

  .brand-small { left: 426px; top: 36px; width: 110px; display: flex; flex-direction: column; align-items: center; gap: 5px; }
  .brand-small .brand-mark { width: 11px; height: 11px; border-radius: 50%; background: var(--brand-blue); }
  .brand-small .brand-name { font-size: 10px; letter-spacing: 0.6px; }

  .stamp-box { left: 704px; top: 19px; width: 57px; height: 57px; background: var(--stamp); }
  .address-line { left: 460px; width: 304px; height: 1px; background: var(--rule-grey); }
  .address-line--1 { top: 120px; }
  .address-line--2 { top: 154px; }
  .address-line--3 { top: 188px; }
  .address-line--4 { top: 222px; }

  .back-contact { right: 44px; font-size: 14px; color: var(--white); display: flex; align-items: center; gap: 12px; }
  .back-contact svg { width: 11px; height: 11px; fill: var(--white); }
  .back-contact--phone { top: 432px; }
  .back-contact--email { top: 457px; }
</style>
</head>
<body>

<section class="postcard postcard--front">
  <svg class="wave" viewBox="0 0 776 501" aria-hidden="true">
    <path d="M430 0 Q520 50 589 70 L589 0 Z" fill="var(--brand-blue)"/>
    <path d="M420 0 Q510 55 589 78" fill="none" stroke="var(--brand-blue)" stroke-width="3"/>
    <path d="M731 0 L776 0 L776 60 Q755 70 731 78 Z" fill="var(--brand-blue)"/>
    <path d="M731 86 Q755 80 776 68" fill="none" stroke="var(--brand-blue)" stroke-width="3"/>
    <path d="M0 350 Q70 290 200 262 Q280 252 310 262 L500 290 Q560 310 640 360 Q720 405 776 440 L776 501 L0 501 Z" fill="var(--brand-blue)"/>
    <path d="M0 337 Q70 277 200 249 Q280 240 310 250" fill="none" stroke="var(--brand-blue)" stroke-width="3"/>
    <path d="M700 410 Q740 430 776 455" fill="none" stroke="var(--white)" stroke-width="4"/>
  </svg>

  <h1 class="headline">DESIGN THE SMILE</h1>
  <div class="rule rule--top"></div>
  <h2 class="subhead">YOUR HOME DESERVES</h2>
  <div class="rule rule--bottom"></div>
  <ul class="feature-row feature-row--1">
    <li>Distinctive style</li><li>Work of Art</li><li>One-of-a-Kind</li><li>Elegant</li>
  </ul>
  <ul class="feature-row feature-row--2">
    <li>Modern</li><li>Innovative</li><li>Unique</li>
  </ul>

  <div class="brand-panel">
    <span class="brand-mark"></span>
    <span class="brand-name">Wrought Gate<br>Studio</span>
  </div>

  <div class="portrait" role="img" aria-label="Portrait photo of Dean Harlowe"></div>

  <p class="contact contact-name">Dean Harlowe</p>
  <p class="contact contact-line contact-line--phone">
    <svg viewBox="0 0 24 24" aria-hidden="true"><path d="M6.6 10.8a15 15 0 0 0 6.6 6.6l2.2-2.2a1 1 0 0 1 1-.25 11.4 11.4 0 0 0 3.6.57 1 1 0 0 1 1 1V20a1 1 0 0 1-1 1A17 17 0 0 1 3 4a1 1 0 0 1 1-1h3.5a1 1 0 0 1 1 1c0 1.25.2 2.45.57 3.57a1 1 0 0 1-.25 1z"/></svg>
    (555)-318-2764
  </p>
  <p class="contact contact-line contact-line--email">
    <svg viewBox="0 0 24 24" aria-hidden="true"><path d="M2 5h20v14H2z M4 7v.5l8 5 8-5V7z" fill-rule="evenodd"/></svg>
    Dean@wroughtgatestudio.example
  </p>

  <div class="door-floor"></div>
  <div class="door door--ornate" role="img" aria-label="3D render of an ornate double iron door with sweeping curved bars over frosted glass"></div>
  <div class="door door--modern" role="img" aria-label="3D render of a modern iron door with horizontal glass slots, sidelights and transom"></div>
</section>

<section class="postcard postcard--back">
  <svg class="wave" viewBox="0 0 776 501" aria-hidden="true">
    <path d="M300 501 Q500 380 700 382 Q745 384 776 396 L776 501 Z" fill="var(--brand-blue)"/>
    <path d="M285 501 Q490 370 700 370 Q745 372 776 384" fill="none" stroke="var(--brand-blue)" stroke-width="3"/>
  </svg>

  <div class="gallery-photo photo-before-1" role="img" aria-label="Before: plain white paneled double door under an arched window"></div>
  <div class="gallery-photo photo-after-1" role="img" aria-label="After: arched wrought iron double door with holiday wreaths"></div>
  <div class="gallery-photo photo-before-2" role="img" aria-label="Before: worn wooden double door"></div>
  <div class="gallery-photo photo-after-2" role="img" aria-label="After: black iron double door with scrollwork and amber glass"></div>
  <p class="photo-label label-before-1">Before</p>
  <p class="photo-label label-after-1">After</p>
  <p class="photo-label label-before-2">Before</p>
  <p class="photo-label label-after-2">After</p>

  <div class="brand-small">
    <span class="brand-mark"></span>
    <span class="brand-name">Wrought Gate<br>Studio</span>
  </div>

  <div class="stamp-box"></div>
  <div class="address-line address-line--1"></div>
  <div class="address-line address-line--2"></div>
  <div class="address-line address-line--3"></div>
  <div class="address-line address-line--4"></div>

  <p class="back-contact back-contact--phone">
    (555)-318-2764
    <svg viewBox="0 0 24 24" aria-hidden="true"><path d="M6.6 10.8a15 15 0 0 0 6.6 6.6l2.2-2.2a1 1 0 0 1 1-.25 11.4 11.4 0 0 0 3.6.57 1 1 0 0 1 1 1V20a1 1 0 0 1-1 1A17 17 0 0 1 3 4a1 1 0 0 1 1-1h3.5a1 1 0 0 1 1 1c0 1.25.2 2.45.57 3.57a1 1 0 0 1-.25 1z"/></svg>
  </p>
  <p class="back-contact back-contact--email">
    Dean@wroughtgatestudio.example
    <svg viewBox="0 0 24 24" aria-hidden="true"><path d="M2 5h20v14H2z M4 7v.5l8 5 8-5V7z" fill-rule="evenodd"/></svg>
  </p>
</section>

</body>
</html>
```